FRESH WEB DESIGN FOR A HEALTH - SOCIAL NETWORK

We are currently looking for a creative, fresh, vibrant, inspiring design for a new social network focused on health and nutrition for health professionals (namely nutritionists) and end-users.

Design requirements - IMPORTANT: please see attached file 'LumaGrove web site design scope' for the detailed brief.

The web site requires new design templates with inter-changeable banners and in some cases profile images. It's important for the website to communicate LumaGrove's core values and image which includes fun, vitality, freshness, life fulfillment, trust, integrity and loyalty to the two target groups. Imagery must have a consistent/inter-related theme across all communities, topics and resources, which need to be easily applied to the web site.To help engage our audience we are looking for something fresh and unique in the selected imagery/ theme/ design templates.

The chosen design will need to be applied to create a PDF, PowerPoint and business card template.

Please see attached file 'LumaGrove web site design scope' to view the LumaGrove web site, which is currently under development.

Industry/Entity Type

Nutrition

```html
<!DOCTYPE html>
<html lang="en">
<head>
<meta charset="utf-8">
<title>LumaGrove — Health Community</title>
<link rel="stylesheet" href="https://fonts.googleapis.com/css2?family=Open+Sans:ital,wght@0,400;0,600;0,700;1,400&display=swap">
<style>
  :root {
    --blue: #1ba0d8;
    --green: #9dc32a;
    --text: #7a7a7a;
    --dark: #2b2b2b;
    --light: #f2f2f2;
    --band: #e6e6e6;
    --white: #ffffff;
  }
  * { box-sizing: border-box; margin: 0; padding: 0; }
  html, body { width: 735px; height: 1200px; overflow: hidden; }
  body { font-family: "Open Sans", Arial, sans-serif; background: var(--white); position: relative; }
  section, header, footer { position: absolute; left: 0; width: 735px; }

  .site-header { top: 0; height: 41px; background: var(--white); }
  .brand { position: absolute; left: 54px; top: 9px; display: flex; align-items: center; gap: 6px;
    font-size: 19px; font-weight: 600; color: var(--green); }
  .brand-dot { width: 14px; height: 14px; border-radius: 50%; background: var(--blue); }
  .account-links { position: absolute; right: 55px; top: 14px; font-size: 10px; font-weight: 700; letter-spacing: .3px; }
  .account-links .login { color: var(--green); }
  .account-links .sep { color: var(--blue); margin: 0 6px; }
  .account-links .register { color: var(--blue); }

  .hero { top: 41px; height: 342px; overflow: hidden; }
  .hero-photo { position: absolute; inset: 0;
    background: linear-gradient(180deg, #4d6a48 0%, #5b6750 40%, #3f4a55 75%, #4f6a3c 100%); }
  .hero-shade { position: absolute; inset: 0; background: rgba(0,0,0,.3); }
  .hero-title { position: absolute; top: 162px; width: 100%; text-align: center; color: var(--white);
    font-size: 32px; font-weight: 700; letter-spacing: .3px; }
  .hero-sub { position: absolute; top: 211px; width: 100%; text-align: center; color: var(--white);
    font-size: 10px; font-weight: 600; }
  .search { position: absolute; left: 54px; top: 243px; width: 626px; height: 39px;
    background: rgba(0,0,0,.55); border: 1px solid rgba(255,255,255,.25); border-radius: 3px; }
  .search-input { position: absolute; left: 3px; top: 3px; width: 535px; height: 32px; background: var(--white);
    border-radius: 2px; font-size: 11.5px; color: #888; padding: 8px 11px; }
  .search-button { position: absolute; left: 542px; top: 3px; width: 82px; height: 32px; background: var(--green);
    color: var(--white); font-size: 11px; font-weight: 700; display: flex; align-items: center; justify-content: center; gap: 4px; }

  .section-title { position: absolute; width: 100%; text-align: center; font-size: 16px; font-weight: 700; color: var(--blue); }
  .section-title .accent { color: var(--green); }
  .divider { position: absolute; left: 305px; width: 125px; height: 3px; }
  .divider .rule { position: absolute; top: 0; height: 2px; background: #c8c8c8; }
  .divider .rule.left { left: 0; width: 55px; }
  .divider .rule.right { right: 0; width: 55px; }
  .divider .mark { position: absolute; left: 57px; width: 12px; height: 3px; background: var(--blue); }

  .about { top: 383px; height: 183px; background: var(--light); }
  .about .section-title { top: 22px; }
  .about .divider { top: 50px; }
  .about-text { position: absolute; left: 54px; top: 64px; width: 627px; text-align: center;
    font-size: 9.4px; line-height: 16.3px; color: var(--text); }

  .community { top: 566px; height: 476px; background: var(--white); }
  .community .section-title { top: 20px; }
  .community .divider { top: 48px; }
  .community-text { position: absolute; left: 92px; top: 61px; width: 551px; text-align: center;
    font-size: 11.5px; line-height: 18.5px; color: var(--text); white-space: nowrap; }
  .learn-more { position: absolute; left: 311px; top: 109px; width: 113px; height: 27px; background: var(--green);
    color: var(--white); font-size: 11px; font-weight: 700; display: flex; align-items: center; justify-content: center; }
  .video { position: absolute; left: 107px; top: 152px; width: 521px; height: 292px; overflow: hidden;
    background: linear-gradient(135deg, #8a8e8c 0%, #6e7472 45%, #4e5557 100%); }
  .video-shade { position: absolute; inset: 0; background: rgba(0,0,0,.25); }
  .play { position: absolute; left: 226px; top: 112px; }

  .join { top: 1042px; height: 114px; background: var(--band); }
  .join .section-title { top: 21px; }
  .join .divider { top: 44px; }
  .field { position: absolute; top: 61px; width: 246px; height: 30px; background: var(--light);
    font-size: 10px; font-style: italic; color: #9a9a9a; padding: 8px 12px; }
  .field.email { left: 66px; }
  .field.password { left: 322px; }
  .signup { position: absolute; left: 586px; top: 61px; width: 95px; height: 30px; background: var(--blue);
    color: var(--white); font-size: 11.5px; font-weight: 700; display: flex; align-items: center; justify-content: center; }

  .site-footer { top: 1156px; height: 44px; background: var(--dark); }
  .legal { position: absolute; left: 53px; top: 17px; font-size: 7.4px; color: #9a9a9a; }
  .legal .name-blue { color: var(--blue); }
  .legal .pipe { margin: 0 6px; }
  .social { position: absolute; right: 53px; top: 14px; display: flex; gap: 10px; }
  .social span { width: 13px; height: 13px; background: #bfbfbf; border-radius: 50%; display: block; }
  .social span.first { background: var(--blue); border-radius: 1px; }
</style>
</head>
<body>
  <header class="site-header">
    <div class="brand"><span class="brand-dot"></span>LumaGrove</div>
    <nav class="account-links"><span class="login">LOGIN</span><span class="sep">/</span><span class="register">REGISTER</span></nav>
  </header>

  <section class="hero">
    <div class="hero-photo" role="img" aria-label="Photo of a smiling family outdoors, parents giving their daughters piggyback rides in a green park"></div>
    <div class="hero-shade"></div>
    <h1 class="hero-title">JOIN THE LUMA GROVE</h1>
    <p class="hero-sub">Lorem ipsum dolor sit amet, consectetur adipiscing elit. Nullam scelerisque dapibus tincidunt.</p>
    <div class="search">
      <div class="search-input">Search...</div>
      <div class="search-button">
        <svg width="16" height="16" viewBox="0 0 16 16" aria-hidden="true"><circle cx="6.5" cy="6.5" r="4.8" fill="none" stroke="#fff" stroke-width="1.8"/><line x1="10" y1="10" x2="14.5" y2="14.5" stroke="#fff" stroke-width="2.2" stroke-linecap="round"/></svg>
        SEARCH
      </div>
    </div>
  </section>

  <section class="about">
    <h2 class="section-title">ABOUT <span class="accent">LUMA GROVE</span></h2>
    <div class="divider"><span class="rule left"></span><span class="mark"></span><span class="rule right"></span></div>
    <p class="about-text">Lorem ipsum dolor sit amet, consectetur adipiscing elit. Nullam scelerisque dapibus tincidunt. Etiam bibendum molestie dui, non luctus justo dapibus eget. Mauris augue dui, ultricies vehicula sapien sit amet, finibus venenatis libero. Integer vehicula rhoncus neque eget vestibulum. Sed consectetur est vitae lacinia faucibus. Nunc vestibulum malesuada neque ac volutpat. Vestibulum condimentum quam enim, non imperdiet orci eleifend eget. Maecenas turpis nisl, tempus tincidunt nisl vel, accumsan aliquet purus. Vestibulum finibus consectetur enim, a tincidunt massa lobortis at. Interdum et malesuada fames ac ante ipsum primis in faucibus. In dui lacus, vehicula eu convallis ut, eleifend sed odio. Vivamus vel congue lorem. Mauris faucibus massa quis commodo molestie. Aenean tempor sit amet nisl ac feugiat.</p>
  </section>

  <section class="community">
    <h2 class="section-title">START A <span class="accent">HEALTH COMMUNITY</span></h2>
    <div class="divider"><span class="rule left"></span><span class="mark"></span><span class="rule right"></span></div>
    <p class="community-text">Lorem ipsum dolor sit amet, consectetur adipiscing elit. Nullam scelerisque<br>dapibus tincidunt. Etiam bibendum molestie dui, non luctus justo dapibus eget.</p>
    <div class="learn-more">LEARN MORE</div>
    <div class="video">
      <div class="video-shade" role="img" aria-label="Video still of a joyful woman stretching her arms wide in a bright, airy setting"></div>
      <svg class="play" width="69" height="69" viewBox="0 0 69 69" aria-label="Play video">
        <circle cx="34.5" cy="34.5" r="32.5" fill="none" stroke="#fff" stroke-width="2.5"/>
        <polygon points="27,20 27,49 51,34.5" fill="#fff"/>
      </svg>
    </div>
  </section>

  <section class="join">
    <h2 class="section-title">JOIN <span class="accent">LUMA GROVE</span></h2>
    <div class="divider"><span class="rule left"></span><span class="mark"></span><span class="rule right"></span></div>
    <div class="field email">Email</div>
    <div class="field password">Password</div>
    <div class="signup">SIGN UP</div>
  </section>

  <footer class="site-footer">
    <p class="legal">© 2014-2015, <span class="name-blue">LUMA GROVE</span>. All rights reserved.<span class="pipe">|</span>Privacy Policy&nbsp; / &nbsp;Terms of Use</p>
    <div class="social" aria-label="Social links">
      <span class="first"></span><span></span><span></span><span></span><span></span><span></span>
    </div>
  </footer>
</body>
</html>
```